Business Card Design for Photographer

Updating business card design. Must use included logo. We're a luxury wedding photography business. Elegancy, luxury, consistency are messages we wish to convey.

Visit our website at www.colbyvarnway.com to familiarize yourself more with our brand design currently (fonts, colors etc.). This is what we want to maintain.

Target Market(s)

Luxury Brides and Grooms

Industry/Entity Type

Wedding

Contact Information for Business Card

Current logo (attached to brief)
Name: Colby Varnway
Phone: 5208813047
website/blog
Email

Requirements
Must have
• Current logo (attached to brief)
• Name: Colby Varnway
• Phone: 5208813047
• website/blog
• Email
• Photoline username
Should not have
• bright colors, fonts that don't suit our brand (visit www.colbyvarnway.com)

```html
<!DOCTYPE html>
<html lang="en">
<head>
<meta charset="utf-8">
<title>Colby Varnway – Business Card</title>
<link href="https://fonts.googleapis.com/css2?family=Amarante&family=Noticia+Text:ital,wght@1,400;1,700&display=swap" rel="stylesheet">
<style>
  :root {
    --canvas: #ffffff;
    --edge: #d6d6d6;
    --ink-dark: #2e2e2e;
    --ink-soft: #3a3a3a;
    --mark: #3c3c3c;
    --photo-light: #fdfbf7;
    --photo-warm: #f4dcc0;
    --photo-deep: #8a6f5c;
    --tulle-light: #fbf1e8;
    --tulle-warm: #efd6c3;
  }
  * { margin: 0; padding: 0; box-sizing: border-box; }
  html, body {
    width: 1200px; height: 375px; overflow: hidden;
    background: var(--canvas);
  }
  .sheet { position: relative; width: 1200px; height: 375px; }
  .card {
    position: absolute; top: 2px; height: 371px; width: 593px;
    border: 1px solid var(--edge); overflow: hidden;
  }
  .card--front { left: 1px; }
  .card--back { left: 601px; }

  .front-photo {
    position: absolute; inset: 0;
    background:
      radial-gradient(ellipse 45% 70% at 72% 45%, rgba(138,111,92,0.55), rgba(138,111,92,0) 70%),
      linear-gradient(90deg, var(--photo-light) 0%, var(--photo-light) 30%, var(--photo-warm) 55%, #e8cbb0 80%, #cfb39c 100%);
  }
  .front-mark {
    position: absolute; left: 176px; top: 90px;
    display: flex; align-items: center; gap: 10px;
  }
  .front-mark__square { width: 48px; height: 48px; background: var(--mark); }
  .front-mark__name {
    font-family: "Amarante", serif; font-size: 14px; color: var(--mark);
  }
  .front-name {
    position: absolute; left: 51px; top: 186px;
    font-family: "Amarante", serif; font-weight: 400; font-size: 36px; letter-spacing: 3.5px;
    color: var(--ink-dark); text-transform: uppercase; white-space: nowrap;
  }
  .front-role {
    position: absolute; left: 28px; top: 243px;
    font-family: "Amarante", serif; font-size: 16px; letter-spacing: 1.8px;
    color: var(--ink-dark); text-transform: uppercase; white-space: nowrap;
  }

  .back-texture {
    position: absolute; inset: 0;
    background:
      radial-gradient(ellipse 60% 50% at 30% 70%, rgba(239,214,195,0.9), rgba(239,214,195,0) 70%),
      radial-gradient(ellipse 50% 40% at 80% 30%, rgba(233,205,186,0.8), rgba(233,205,186,0) 70%),
      linear-gradient(160deg, var(--tulle-light), var(--tulle-warm));
  }
  .contact {
    position: absolute; inset: 0; list-style: none;
    font-family: "Noticia Text", serif; font-style: italic;
    color: var(--ink-soft); text-align: center;
  }
  .contact li { position: absolute; left: 0; right: 0; font-size: 20px; line-height: 28px; white-space: nowrap; }
  .contact__name { top: 56px; font-weight: 700; }
  .contact__phone { top: 101px; }
  .contact__phone svg { width: 19px; height: 19px; vertical-align: -3px; margin-right: 5px; }
  .contact__web { top: 147px; }
  .contact__email { top: 192px; }
  .contact__social-a { top: 237px; }
  .contact__social-b { top: 282px; }
</style>
</head>
<body>
<main class="sheet">
  <section class="card card--front">
    <div class="front-photo" role="img" aria-label="Sunlit photograph of an embracing couple by the water"></div>
    <div class="front-mark">
      <div class="front-mark__square"></div>
      <span class="front-mark__name">Colby Varnway</span>
    </div>
    <h1 class="front-name">Colby Varnway</h1>
    <p class="front-role">Portrait &amp; Wedding Photographer</p>
  </section>

  <section class="card card--back">
    <div class="back-texture" role="img" aria-label="Soft blush tulle fabric background"></div>
    <ul class="contact">
      <li class="contact__name">COLBY VARNWAY</li>
      <li class="contact__phone"><svg viewBox="0 0 20 20" aria-hidden="true"><circle cx="10" cy="10" r="8.5" fill="none" stroke="currentColor" stroke-width="1.3"/><path d="M7.2 5.5l1.6 2.2-1 1.1c.6 1.3 1.5 2.2 2.6 2.8l1.1-1 2.1 1.5-.9 1.9c-3.4-.4-6.1-3.3-6.4-6.8z" fill="currentColor"/></svg>+520 881-3047</li>
      <li class="contact__web">website: www.colbyvarnway.com</li>
      <li class="contact__email">email: colby@colbyvarnway.com</li>
      <li class="contact__social-a">Photoline : www.photoline.net/colbyvarnwayphoto</li>
      <li class="contact__social-b">Friendly: www.friendly.net/colbyvarnwayphoto</li>
    </ul>
  </section>
</main>
</body>
</html>
```